We need a letterhead incorporating our logo (uploaded file), with the name of our organization (Ashbourne Vale Borough Police Association) and our slogan (Strength in Unity). Dark blue should be incorporated somewhere in the design, either the font color or elsewhere. Please make sure our logo is included in the design. The organization is a law enforcement union type group.

Target Market(s)

Members of our association, policticians, and anyone receiving our letters

Colors
0255a3

Requirements
Must have
• Our logo, Association name, and slogan.
Nice to have
• A professional and eye-catching letterhead design incorporating the logo, name, and slogan.

```html
<!DOCTYPE html>
<html lang="en">
<head>
<meta charset="utf-8">
<title>Ashbourne Vale Borough Police Association – Letterhead</title>
<link href="https://fonts.googleapis.com/css2?family=Montserrat:wght@500;700&family=Comfortaa:wght@500&family=Poppins:wght@400&display=swap" rel="stylesheet">
<style>
  :root {
    --blue: #0255a3;
    --line-blue: #2a4fa8;
    --orange: #f7be7c;
    --ink: #2b2b2b;
    --paper: #ffffff;
    --backdrop: #e4e4e6;
  }
  * { box-sizing: border-box; margin: 0; padding: 0; }
  html, body { width: 1200px; height: 1200px; overflow: hidden; }
  body { background: var(--backdrop); position: relative; }

  .letter {
    position: absolute; left: 175px; top: 50px;
    width: 850px; height: 1100px;
    background: var(--paper);
    box-shadow: 0 6px 24px rgba(0,0,0,.12);
    overflow: hidden;
  }

  .header-band {
    position: absolute; left: 0; right: 0; top: 62px; height: 62px;
    display: flex;
  }
  .band-name {
    flex: 0 0 560px; background: var(--blue);
    padding-left: 238px;
    display: flex; flex-direction: column; justify-content: center;
    color: #fff; font-family: 'Montserrat', sans-serif;
    white-space: nowrap;
  }
  .band-name .org-name { font-weight: 700; font-size: 19px; letter-spacing: 1px; line-height: 1.2; }
  .band-name .org-sub { font-weight: 500; font-size: 10.5px; letter-spacing: 4px; padding-left: 40px; margin-top: 2px; }
  .band-slogan {
    flex: 1; background: var(--orange);
    display: flex; align-items: center; justify-content: center;
    padding: 0 18px;
    font-family: 'Comfortaa', sans-serif; font-size: 18px; letter-spacing: 1.2px;
    color: var(--ink); text-transform: uppercase; white-space: nowrap;
  }

  .logo-seal {
    position: absolute; left: 92px; top: 28px;
    width: 130px; height: 130px; border-radius: 50%;
    background: #fff; border: 6px solid var(--blue);
  }

  .footer { position: absolute; left: 0; top: 940px; width: 850px; height: 130px; }
  .contact-list {
    position: absolute; left: 120px; right: 60px; top: 52px;
    display: flex; gap: 70px;
    font-family: 'Poppins', sans-serif; font-size: 12px; color: var(--ink); line-height: 1.5;
    white-space: nowrap;
  }
  .contact-item { display: flex; align-items: center; gap: 14px; }
  .contact-item svg { flex: 0 0 30px; }
</style>
</head>
<body>
  <main class="letter">
    <div class="header-band">
      <div class="band-name">
        <span class="org-name">ASHBOURNE VALE BOROUGH</span>
        <span class="org-sub">POLICE ASSOCIATION</span>
      </div>
      <div class="band-slogan">Strength in Unity</div>
    </div>
    <div class="logo-seal" aria-hidden="true"></div>

    <footer class="footer">
      <svg class="footer-rules" width="850" height="130" viewBox="0 0 850 130">
        <line x1="55" y1="30" x2="790" y2="30" stroke="var(--line-blue)" stroke-width="1.5"/>
        <rect x="55" y="26" width="80" height="8" fill="var(--blue)"/>
        <line x1="120" y1="112" x2="800" y2="112" stroke="var(--line-blue)" stroke-width="1.5"/>
        <rect x="735" y="108" width="80" height="8" fill="var(--blue)"/>
      </svg>
      <div class="contact-list">
        <div class="contact-item">
          <svg width="30" height="30" viewBox="0 0 30 30"><circle cx="15" cy="15" r="15" fill="var(--blue)"/><path d="M11 10c-1 1 0 5 3 8s7 4 8 3l-2-3-2 1c-1 0-4-3-4-4l1-2z" fill="#fff"/></svg>
          <span>555.014.2287<br>555.014.6630</span>
        </div>
        <div class="contact-item">
          <svg width="30" height="30" viewBox="0 0 30 30"><circle cx="15" cy="15" r="15" fill="var(--blue)"/><g fill="none" stroke="#fff" stroke-width="1.2"><circle cx="15" cy="15" r="6"/><ellipse cx="15" cy="15" rx="2.6" ry="6"/><line x1="9" y1="15" x2="21" y2="15"/></g></svg>
          <span>info@avbpa.org<br>www.avbpa.org</span>
        </div>
        <div class="contact-item">
          <svg width="30" height="30" viewBox="0 0 30 30"><circle cx="15" cy="15" r="15" fill="var(--blue)"/><path d="M15 8a5 5 0 0 0-5 5c0 4 5 9 5 9s5-5 5-9a5 5 0 0 0-5-5z" fill="#fff"/><circle cx="15" cy="13" r="1.8" fill="var(--blue)"/></svg>
          <span>42 Linden Court, Harrow Lane,<br>Ashbourne 20417</span>
        </div>
      </div>
    </footer>
  </main>
</body>
</html>
```